Wellness bold & beautiful PowerPoint Template

I will like a PowerPoint template, matching my brand, designed for my business.
- Some words that describe our brand identity are: wellness, natural, calming, simplicity, clean
- For icons, we prefer line icons.
- Website: http://www.verinaxo.com/
- PowerPoint board: https://www.pinboardly.com/tesmaruli/verinaxo-powerpoint/
- Branding board: https://www.pinboardly.com/tesmaruli/verinaxo-branding/
FYI: I am attaching a rough draft of a powerpoint presentation we are preparing
Target Market(s)
Women 23-48 interested in wellness
Industry/Entity Type
Health And Wellness
Font styles to use
Other font styles liked:
- Open Sans, Helvitica, Meddon
Requirements
Must have
- cover page, about page, author page, table of content, table format, graph format, list format, 2 column template.
Nice to have
- time line page sample

```html
<!DOCTYPE html>
<html lang="en">
<head>
<meta charset="utf-8">
<title>Verinaxo Wellness PowerPoint Template</title>
<link rel="stylesheet" href="https://fonts.googleapis.com/css2?family=Oswald:wght@200&family=Open+Sans:ital,wght@0,400;0,600;0,700;1,800&display=swap">
<style>
:root{
  --canvas:#6e6e6c;
  --white:#ffffff;
  --magenta:#b0267f;
  --green:#18a048;
  --teal:#4cb8a0;
  --ink:#2b2b2b;
  --muted:#6a6a6a;
  --rule:#cfd8d6;
  --bar-bg:#e4e4e4;
  --badge:#e3f1ec;
}
*{box-sizing:border-box;margin:0;padding:0}
html,body{width:1200px;height:1200px;overflow:hidden;background:var(--canvas)}
body{position:relative;font-family:"Open Sans",Helvetica,Arial,sans-serif;color:var(--ink)}
.slide{position:absolute;overflow:hidden;background:var(--white)}
.abs{position:absolute}
.photo{position:absolute}
.photo--dandelion{background:linear-gradient(160deg,#c66aa8 0%,#8a3d86 40%,#5b2a5e 75%,#7a4c7a 100%)}
.photo--leaf{background:radial-gradient(ellipse at 75% 30%,#7fa86a 0%,#3f7a4c 45%,#2a5b44 100%)}
.photo--road{background:linear-gradient(180deg,#9ea23a 0%,#6f7430 40%,#5a3b2a 70%,#2e2a26 100%)}
.photo--meadow{background:linear-gradient(170deg,#6e6a3e 0%,#3f4a36 50%,#2a3028 100%)}
.photo--pattern{background:linear-gradient(90deg,#6d8a62 0%,#8c7a5e 45%,#b45a6a 70%,#c98a7a 100%)}
.photo--portrait{background:linear-gradient(180deg,#c9a48c,#8c6a58)}
.panel-magenta{background:var(--magenta)}
.panel-green{background:var(--green)}
.big-title{font-family:Oswald,"Arial Narrow",sans-serif;font-weight:200;text-transform:uppercase;line-height:.92;letter-spacing:-1px}
.badge{position:absolute;border-radius:50%;background:var(--badge);border:2px solid var(--white)}
.wordmark{font-family:"Open Sans",Helvetica,sans-serif;font-weight:600;letter-spacing:.5px}
.corner-mark{position:absolute;right:12px;bottom:8px;font-size:8px;color:var(--magenta)}
.url{font-size:4px;color:var(--muted)}
.body-text{font-size:4.2px;line-height:1.4;color:var(--muted)}
.body-white{font-size:4.2px;line-height:1.4;color:rgba(255,255,255,.85)}
.item-title{font-weight:800;font-style:italic;font-size:7px;color:var(--ink)}
.label{font-size:4px;color:var(--muted)}
.bar{position:absolute;height:1.5px;background:var(--bar-bg)}
.bar i{display:block;height:100%}
.fill-teal{background:var(--teal)}
.fill-dark{background:var(--ink)}
.fill-magenta{background:var(--magenta)}
.fill-purple{background:#6a3d8c}
.flag{position:absolute;width:0;height:0;border-style:solid}
.timeline-rule{position:absolute;width:1px;background:#bfe0d8}
.year{position:absolute;font-size:5px;color:var(--muted)}
</style>
</head>
<body>

<!-- Cover -->
<section class="slide" style="left:16px;top:18px;width:336px;height:188px">
  <div class="photo photo--dandelion" style="inset:0" role="img" aria-label="Dandelion meadow in soft purple light"></div>
  <div class="badge" style="left:146px;top:40px;width:46px;height:46px"></div>
  <div class="abs wordmark" style="left:0;width:336px;top:102px;text-align:center;color:var(--white);font-size:14px">verinaxo</div>
  <div class="abs" style="left:0;width:336px;top:124px;text-align:center;color:var(--white);font-size:7.5px;letter-spacing:2.5px">PRESENTATION</div>
</section>

<!-- Title -->
<section class="slide" style="left:395px;top:18px;width:344px;height:193px">
  <div class="photo photo--leaf" style="inset:0" role="img" aria-label="Willow leaves over a blurred green background"></div>
  <div class="badge" style="left:62px;top:66px;width:46px;height:46px"></div>
  <div class="abs" style="left:130px;top:66px;width:1px;height:48px;background:rgba(255,255,255,.6)"></div>
  <div class="abs wordmark" style="left:140px;top:74px;color:var(--white);font-size:13px">verinaxo</div>
  <div class="abs" style="left:140px;top:93px;color:var(--white);font-size:11px;letter-spacing:2.5px">POWERPOINT</div>
  <div class="abs body-white" style="left:140px;top:108px;width:160px">Far away, behind the hills, far from the calm countries.</div>
</section>

<!-- Contents -->
<section class="slide" style="left:786px;top:18px;width:345px;height:194px">
  <div class="photo photo--road" style="inset:0" role="img" aria-label="Open road through a desert valley at dusk"></div>
  <div class="badge" style="left:68px;top:36px;width:90px;height:90px"></div>
  <div class="abs wordmark" style="left:80px;top:128px;color:var(--white);font-size:12px">verinaxo</div>
  <div class="abs" style="left:205px;top:32px;width:120px;color:var(--white)">
    <div style="font-weight:800;font-style:italic;font-size:11px">01.</div>
    <div class="body-white">Your text &nbsp; Far away<br>Your text &nbsp; Behind the hills</div>
    <div style="font-weight:800;font-style:italic;font-size:11px;margin-top:6px">02.</div>
    <div class="body-white">Your text &nbsp; Far away<br>Your text &nbsp; Behind the calm hills</div>
    <div style="font-weight:800;font-style:italic;font-size:11px;margin-top:8px">03.</div>
    <div class="body-white">Your text &nbsp; Far away<br>Your text &nbsp; Behind the hills<br>Your text &nbsp; Far from the quiet lands</div>
    <div style="font-weight:800;font-style:italic;font-size:11px;margin-top:8px">04.</div>
    <div class="body-white">Your text &nbsp; Far away</div>
  </div>
</section>

<!-- Our awesome team -->
<section class="slide" style="left:18px;top:253px;width:336px;height:189px">
  <div class="abs big-title" style="left:30px;top:28px;font-size:27px;color:var(--ink)">Our<br>Awesome<br>Team</div>
  <div class="abs body-text" style="left:30px;top:105px;width:48px">Far away, behind the word hills, far from the countries, there live the blind texts in a quiet place near the large calm ocean.</div>
  <svg class="abs" style="left:100px;top:0" width="236" height="189" viewBox="0 0 236 189" role="img" aria-label="Diagonal strips of a team photo on patterned ground">
    <defs><linearGradient id="stripe" x1="0" y1="0" x2="1" y2="1"><stop offset="0" stop-color="#c47a9a"/><stop offset=".5" stop-color="#8a3a6a"/><stop offset="1" stop-color="#c79070"/></linearGradient></defs>
    <g fill="url(#stripe)">
      <polygon points="150,0 215,0 140,40 110,40"/>
      <polygon points="190,10 240,10 130,70 95,70"/>
      <polygon points="215,30 240,30 90,110 60,110"/>
      <polygon points="220,55 240,55 110,125 85,125"/>
      <polygon points="230,70 240,70 40,160 20,160"/>
      <polygon points="225,95 240,95 100,170 80,170"/>
      <polygon points="230,115 236,115 120,178 105,178"/>
    </g>
  </svg>
  <div class="corner-mark wordmark">verinaxo</div>
</section>

<!-- Single team -->
<section class="slide" style="left:395px;top:253px;width:346px;height:194px">
  <div class="abs panel-magenta" style="left:0;top:0;width:104px;height:194px"></div>
  <div class="abs big-title" style="left:0;width:86px;top:22px;text-align:right;font-size:24px;color:var(--white)">Single<br>Team<br>Slide</div>
  <div class="flag" style="left:80px;top:98px;border-width:0 8px 8px 0;border-color:transparent var(--green) transparent transparent"></div>
  <div class="badge" style="left:28px;top:104px;width:58px;height:58px"></div>
  <div class="abs" style="left:54px;top:166px;width:34px;height:1px;background:rgba(255,255,255,.5)"></div>
  <div class="abs url" style="left:52px;top:170px;color:var(--white)">www.verinaxo.com</div>
  <div class="photo photo--meadow" style="left:104px;top:0;width:242px;height:194px" role="img" aria-label="Dandelion seed heads in a dark green field"></div>
  <div class="abs body-white" style="left:254px;top:60px;width:60px">Far away, behind the word hills, far from the calm lands there live the texts.<br><br>Separated they live by the coast of a large ocean.<br><br>- The Quotes</div>
  <div class="abs" style="left:254px;top:142px;font-size:3.5px;color:var(--white)">Wellness</div>
  <div class="bar" style="left:254px;top:148px;width:56px"><i class="fill-teal" style="width:80%"></i></div>
  <div class="abs" style="left:254px;top:152px;font-size:3.5px;color:var(--white)">Health</div>
  <div class="bar" style="left:254px;top:158px;width:56px"><i style="width:70%;background:var(--white)"></i></div>
  <div class="abs" style="left:254px;top:176px;font-size:5px;color:var(--white);letter-spacing:2px">□□□□□</div>
</section>

<!-- Three picture -->
<section class="slide" style="left:786px;top:253px;width:349px;height:195px">
  <div class="abs panel-green" style="left:0;top:0;width:105px;height:195px"></div>
  <div class="abs big-title" style="left:0;width:88px;top:22px;text-align:right;font-size:24px;color:var(--white)">Three<br>Picture<br>Slide</div>
  <div class="flag" style="left:80px;top:98px;border-width:0 8px 8px 0;border-color:transparent var(--magenta) transparent transparent"></div>
  <div class="abs url" style="left:54px;top:168px;color:var(--white)">www.verinaxo.com</div>
  <svg class="abs" style="left:128px;top:28px" width="200" height="60" viewBox="0 0 200 60">
    <g class="photo--portrait">
      <polygon points="34,4 57,16 57,44 34,56 11,44 11,16" fill="#b4876e" role="img" aria-label="Team member portrait"/>
      <polygon points="108,4 131,16 131,44 108,56 85,44 85,16" fill="#a88572" role="img" aria-label="Team member portrait"/>
      <polygon points="182,4 205,16 205,44 182,56 159,44 159,16" fill="#b99580" role="img" aria-label="Team member portrait"/>
    </g>
  </svg>
  <div class="abs" style="left:138px;top:92px;width:200px;display:flex;justify-content:space-between;text-align:center">
    <div style="width:52px"><div style="font-size:6px">YOUR TITLE</div><div class="label">Founder</div><div class="body-text" style="margin-top:12px">Far away, behind the word hills, far from the lands there live the texts.</div><div style="font-size:5px;letter-spacing:1.5px;margin-top:4px">□□□□□</div></div>
    <div style="width:52px"><div style="font-size:6px">YOUR TITLE</div><div class="label">Founder</div><div class="body-text" style="margin-top:12px">Far away, behind the word hills, far from the lands there live the texts.</div><div style="font-size:5px;letter-spacing:1.5px;margin-top:4px">□□□□□</div></div>
    <div style="width:52px"><div style="font-size:6px">YOUR TITLE</div><div class="label">Founder</div><div class="body-text" style="margin-top:12px">Far away, behind the word hills, far from the lands there live the texts.</div><div style="font-size:5px;letter-spacing:1.5px;margin-top:4px">□□□□□</div></div>
  </div>
  <div class="corner-mark wordmark">verinaxo</div>
</section>

<!-- Two picture A -->
<section class="slide" style="left:18px;top:474px;width:340px;height:192px">
  <div class="abs big-title" style="left:0;width:146px;top:24px;text-align:right;font-size:24px;color:var(--ink)">Two<br>Picture<br>Slide</div>
  <div class="flag" style="left:138px;top:98px;border-width:0 6px 6px 0;border-color:transparent var(--teal) transparent transparent"></div>
  <div class="abs body-text" style="left:30px;top:120px;width:116px;text-align:right">Far away, behind the word hills, far from the calm countries, there live the blind texts. Separated they live by the coast of the ocean.</div>
  <div class="abs" style="left:110px;top:152px;width:36px;height:1px;background:var(--rule)"></div>
  <div class="abs url" style="left:104px;top:156px">www.verinaxo.com</div>
  <div class="photo photo--meadow" style="left:160px;top:25px;width:66px;height:112px" role="img" aria-label="Dandelions in a meadow"></div>
  <div class="photo photo--leaf" style="left:238px;top:25px;width:66px;height:112px" role="img" aria-label="Willow leaves on green"></div>
  <div class="abs" style="left:160px;top:144px;width:66px;text-align:center"><div class="item-title" style="font-size:5px">YOUR TITLE</div><div class="body-text">Far away, behind the word hills.</div></div>
  <div class="abs" style="left:238px;top:144px;width:66px;text-align:center"><div class="item-title" style="font-size:5px">YOUR TITLE</div><div class="body-text">Far away, behind the word hills.</div></div>
  <div class="corner-mark wordmark">verinaxo</div>
</section>

<!-- Two picture B -->
<section class="slide" style="left:395px;top:474px;width:350px;height:196px">
  <div class="abs big-title" style="left:0;width:116px;top:24px;text-align:right;font-size:24px;color:var(--ink)">Two<br>Picture<br>Slide</div>
  <div class="flag" style="left:110px;top:98px;border-width:0 6px 6px 0;border-color:transparent var(--magenta) transparent transparent"></div>
  <div class="badge" style="left:56px;top:106px;width:58px;height:58px"></div>
  <div class="abs url" style="left:82px;top:168px">www.verinaxo.com</div>
  <div class="abs body-text" style="left:155px;top:24px;width:140px;font-style:italic">Far away, behind the word hills, far from the countries, there live the blind texts. Separated they live by the coast of a large ocean.<br><br>A small river flows by their place and supplies it with water.<br><br>- The Quotes</div>
  <div class="photo photo--dandelion" style="left:155px;top:80px;width:70px;height:40px" role="img" aria-label="Dandelions at sunset"></div>
  <div class="photo photo--leaf" style="left:243px;top:80px;width:70px;height:40px" role="img" aria-label="Willow leaves on green"></div>
  <div class="abs" style="left:155px;top:126px"><div class="item-title" style="font-size:5px">Your Title</div><div class="label">Founder</div></div>
  <div class="abs" style="left:243px;top:126px"><div class="item-title" style="font-size:5px">Your Title</div><div class="label">Founder</div></div>
  <div class="bar" style="left:155px;top:146px;width:62px"><i class="fill-teal" style="width:78%"></i></div>
  <div class="bar" style="left:155px;top:156px;width:62px"><i class="fill-dark" style="width:70%"></i></div>
  <div class="bar" style="left:243px;top:146px;width:62px"><i class="fill-teal" style="width:78%"></i></div>
  <div class="bar" style="left:243px;top:156px;width:62px"><i class="fill-dark" style="width:70%"></i></div>
  <div class="corner-mark wordmark">verinaxo</div>
</section>

<!-- Best designer -->
<section class="slide" style="left:786px;top:474px;width:350px;height:197px">
  <div class="photo photo--leaf" style="left:0;top:0;width:350px;height:85px" role="img" aria-label="Blurred willow leaves in soft green light"></div>
  <div class="abs big-title" style="left:0;width:118px;top:110px;text-align:right;font-size:26px;color:var(--ink)">Best<br>Designer</div>
  <div class="abs url" style="left:84px;top:168px">www.verinaxo.com</div>
  <div class="flag" style="left:318px;top:97px;border-width:0 21px 21px 0;border-color:transparent var(--magenta) transparent transparent"></div>
  <div class="abs" style="left:165px;top:104px;width:120px"><div class="item-title" style="font-size:5.5px">Your Title</div><div class="body-text">• Far away, behind the word hills<br>• from the calm countries far away<br>• there live the blind texts</div></div>
  <div class="bar" style="left:165px;top:146px;width:114px"><i class="fill-teal" style="width:82%"></i></div>
  <div class="bar" style="left:165px;top:156px;width:114px"><i class="fill-dark" style="width:72%"></i></div>
  <div class="corner-mark wordmark">verinaxo</div>
</section>

<!-- Timeline 1 -->
<section class="slide" style="left:16px;top:692px;width:349px;height:196px">
  <div class="abs big-title" style="left:0;width:88px;top:24px;text-align:right;font-size:24px;color:var(--ink)">Timeline<br>Picture<br>Slide</div>
  <div class="flag" style="left:82px;top:98px;border-width:0 8px 8px 0;border-color:transparent var(--teal) transparent transparent"></div>
  <div class="badge" style="left:30px;top:104px;width:60px;height:60px"></div>
  <div class="abs url" style="left:54px;top:168px">www.verinaxo.com</div>
  <div class="badge" style="left:129px;top:36px;width:32px;height:32px"></div>
  <div class="timeline-rule" style="left:144px;top:70px;height:126px"></div>
  <div class="abs" style="left:172px;top:44px"><div class="item-title" style="font-size:7.5px">YOUR NAME</div><div class="label">Designer</div></div>
  <div class="year" style="left:124px;top:82px">2015</div>
  <div class="abs" style="left:160px;top:80px;width:150px"><div class="item-title" style="font-size:5.5px">Your Title Goes Here</div><div class="body-text">Far away, behind the word hills, far from the countries, there live the blind texts.</div></div>
  <div class="photo photo--dandelion" style="left:160px;top:111px;width:150px;height:62px" role="img" aria-label="Dandelion meadow at sunset"></div>
</section>

<!-- Timeline 2 -->
<section class="slide" style="left:395px;top:692px;width:355px;height:200px">
  <div class="timeline-rule" style="left:146px;top:0;height:200px"></div>
  <div class="year" style="left:126px;top:22px">2015</div>
  <div class="abs" style="left:162px;top:20px;width:140px"><div class="item-title" style="font-size:5.5px">Your Title Goes Here</div><div class="body-text">Far away, behind the word hills, far from the countries, there live the blind texts.</div></div>
  <div class="photo photo--leaf" style="left:162px;top:60px;width:48px;height:62px" role="img" aria-label="Willow leaves"></div>
  <div class="photo photo--road" style="left:212px;top:60px;width:48px;height:30px" role="img" aria-label="Open road"></div>
  <div class="photo photo--pattern" style="left:212px;top:92px;width:48px;height:30px" role="img" aria-label="Patterned ground"></div>
  <div class="photo photo--leaf" style="left:262px;top:60px;width:80px;height:62px" role="img" aria-label="Willow leaves on green"></div>
  <div class="year" style="left:126px;top:144px">2015</div>
  <div class="abs" style="left:162px;top:142px;width:150px"><div class="item-title" style="font-size:5.5px">Your Title Goes Here</div><div class="body-text">Far away, behind the word hills, far from the countries, there live the blind texts. Separated they live by the coast of the ocean.<br><br>- The Quotes</div></div>
</section>

<!-- Timeline 3 -->
<section class="slide" style="left:786px;top:692px;width:356px;height:200px">
  <div class="timeline-rule" style="left:146px;top:0;height:150px"></div>
  <div class="year" style="left:126px;top:22px">2015</div>
  <div class="abs" style="left:162px;top:20px"><div class="item-title" style="font-size:5.5px">Your Title Goes Here</div></div>
  <div class="abs label" style="left:165px;top:34px">Wellness</div>
  <div class="bar" style="left:165px;top:40px;width:110px"><i class="fill-teal" style="width:82%"></i></div>
  <div class="abs label" style="left:165px;top:43px">Health</div>
  <div class="bar" style="left:165px;top:49px;width:110px"><i class="fill-magenta" style="width:74%"></i></div>
  <div class="abs label" style="left:165px;top:52px">Balance</div>
  <div class="bar" style="left:165px;top:58px;width:110px"><i class="fill-dark" style="width:72%"></i></div>
  <div class="abs label" style="left:165px;top:61px">Yoga</div>
  <div class="bar" style="left:165px;top:67px;width:110px"><i class="fill-purple" style="width:55%"></i></div>
  <div class="abs" style="left:162px;top:80px;width:126px;height:38px;background:#f0f0f0"></div>
  <div class="abs" style="left:174px;top:92px;width:10px;height:12px;border:1px solid #999"></div>
  <div class="abs body-text" style="left:200px;top:88px;width:80px">Far away, behind the word hills, far from the countries, there live the blind texts.</div>
  <div class="badge" style="left:130px;top:150px;width:32px;height:32px"></div>
  <div class="abs" style="left:174px;top:156px"><div class="item-title" style="font-size:7.5px">YOUR NAME</div><div class="label">Designer</div></div>
</section>

<!-- Full picture -->
<section class="slide" style="left:395px;top:930px;width:356px;height:200px">
  <div class="abs panel-magenta" style="left:0;top:0;width:107px;height:200px"></div>
  <div class="abs big-title" style="left:0;width:90px;top:22px;text-align:right;font-size:24px;color:var(--white)">Full<br>Picture<br>Slide</div>
  <div class="flag" style="left:82px;top:98px;border-width:0 8px 8px 0;border-color:transparent var(--green) transparent transparent"></div>
  <div class="badge" style="left:26px;top:104px;width:62px;height:62px"></div>
  <div class="abs url" style="left:54px;top:172px;color:var(--white)">www.verinaxo.com</div>
  <div class="photo photo--pattern" style="left:107px;top:0;width:249px;height:200px" role="img" aria-label="People resting on hexagon-patterned ground"></div>
  <div class="abs body-white" style="left:126px;top:62px;width:60px">Far away, behind the word hills, far from the countries, there live the blind texts.<br><br>Separated they live by the coast of a large ocean.</div>
  <div class="abs" style="left:126px;top:146px;font-size:3.5px;color:var(--white)">Wellness</div>
  <div class="bar" style="left:126px;top:152px;width:56px"><i class="fill-teal" style="width:80%"></i></div>
  <div class="abs" style="left:126px;top:156px;font-size:3.5px;color:var(--white)">Health</div>
  <div class="bar" style="left:126px;top:162px;width:56px"><i style="width:70%;background:var(--white)"></i></div>
</section>

</body>
</html>
```